WTF!!! We need a modern professional website for a business litigation law firm.

We need a modern, clean, professional and uncomplicated website for a new business trial and litigation law firm called "Hallorand Trial Firm PLLC". Website must be mobile optimized for iPad and smartphone. The law firm specializes in counseling and representing large corporations, small businesses and entrepreneurs in and out of the courtroom. Lawyers in the firm serve as Florida counsel and trial counsel to organizations facing claims involving product liability, premises liability, professional liability, vehicle and transportation liability, warranty claims, construction defects and delay claims, complex business disputes, commercial litigation and bid disputes in State and Federal Courts. The website is mainly to provide information about the firm, and should include sections describing the firm, identifying the Industries Served and Areas of Practice ," a separate page identifying the "Professionals", a separate page for "Resources & Advisories," and a traveling "Connect With Us" button a site visitor can click on that will launch an email to the Firm's general email account. The website should allow us to easily modify the content on these pages, and let us add/modify links to external information sources. We will not sell anything or take payments through the website. We do need to be able to easily upload and update photographs of attorneys and add new attorneys names/email hyperlinks as the firm grows. We would like to add developments in the law or success stories easily and quickly, such as through a blog page. On the "Connect With Us" page the website should have hyperlinks to email the Firm, and there should be hyperlinks to email each professional on the "Professionals" page. The website should be viewable on mobile devices without distortion. The law firm focuses on trial work and should have some imagery associated with courtrooms, but the overall theme of the site should be modern, clean, and communicate sophistication and strength. The website should be made in Wordpress. We have uploaded logo files for Hallorand Trial Firm.

Target Market(s)

Corporations and companies that are looking for legal representation. Other attorneys/legal industry.

Industry/Entity Type

Legal Industry

Coding

Coded - Design and coding required

Number of Pages Required

1 page

Font styles to use
Sans Serif

Requirements
Must have
• Simple, clean, sophisticated, modern website that includes the logo, watermark of logo, and the elements described above.
Nice to have
• Pictures of city scape, buildings, courtroom, team members.

```html
<!DOCTYPE html>
<html lang="en">
<head>
<meta charset="utf-8">
<title>Hallorand Trial Firm PLLC</title>
<link href="https://fonts.googleapis.com/css2?family=Montserrat:wght@500;600;700;800&family=Open+Sans:wght@400;600;700&display=swap" rel="stylesheet">
<style>
:root{
  --gold:#c49a5e;
  --gold-dark:#a87c42;
  --ink:#1d1d1d;
  --text:#555;
  --light:#ddd;
  --cream:#f8f1e7;
  --white:#fff;
  --black:#0e0e0e;
}
*{box-sizing:border-box;margin:0;padding:0}
html,body{width:1200px;height:3928px;overflow:hidden}
body{position:relative;font-family:"Open Sans",Arial,sans-serif;color:var(--text);background:var(--white)}
.abs{position:absolute}
.heading{font-family:"Montserrat",Arial,sans-serif;font-weight:800;color:var(--ink);text-transform:uppercase}
.btn{display:inline-block;background:var(--gold);color:var(--white);font-family:"Montserrat",Arial,sans-serif;font-weight:700;font-size:14px;text-transform:uppercase;letter-spacing:.5px;border-radius:24px;padding:12px 30px;text-decoration:none;white-space:nowrap}
.brand-name{font-family:"Montserrat",Arial,sans-serif;font-weight:800;color:var(--ink);font-size:24px;line-height:1.15;text-transform:uppercase}

/* hero */
.hero{left:0;top:0;width:1200px;height:760px;background:linear-gradient(90deg,#2a2119 0%,#3d3024 45%,#5a4a3a 70%,#2c241c 100%)}
.hero-photo{right:60px;top:60px;width:520px;height:640px;background:radial-gradient(ellipse at 50% 40%,#7a6a5c 0%,#3b3128 60%,transparent 75%)}
.brand-box{left:0;top:0;width:220px;height:190px;background:var(--white);border-bottom-right-radius:40px;display:flex;align-items:center;justify-content:center;text-align:center}
.nav{left:328px;top:0;width:872px;height:80px;background:var(--white);border-bottom-left-radius:30px;display:flex;align-items:center;justify-content:space-between;padding:0 14px 0 18px}
.nav a{font-family:"Montserrat",Arial,sans-serif;font-weight:700;font-size:13px;color:var(--ink);text-decoration:none;padding:31px 12px;white-space:nowrap}
.nav a.active{background:var(--gold);color:var(--white)}
.hero-title{left:100px;top:290px;width:600px;text-align:center;font-family:"Montserrat",Arial,sans-serif;font-weight:800;font-size:52px;line-height:60px;color:var(--gold);letter-spacing:2px}
.hero-text{left:180px;top:418px;width:440px;text-align:center;color:#eee;font-size:15px;line-height:23px}
.hero-cta{left:272px;top:510px}
.hero-edge{left:0;top:660px;width:1200px;height:110px}

/* about */
.about-brand{left:200px;top:960px;width:330px;text-align:center}
.about-brand .brand-name{font-size:32px}
.section-head{display:flex;align-items:center;gap:16px;font-size:34px}
.section-head::before{content:"";width:6px;height:44px;background:var(--gold)}
.copy{font-size:15px;line-height:24px}
.copy-strong{color:var(--ink);font-weight:600}
.about-head{left:688px;top:810px}
.about-copy{left:700px;top:880px;width:420px}
.about-copy p{margin-bottom:18px}
.about-btn{left:700px;top:1164px}

/* practice */
.practice{left:0;top:1280px;width:1200px;height:640px;background:var(--cream)}
.center-title{width:1200px;text-align:center;font-size:34px}
.practice-title{left:0;top:1320px}
.card{top:1400px;width:244px;height:380px}
.card-img{left:0;top:0;width:244px;height:290px}
.card-cap{left:18px;top:250px;width:208px;height:120px;background:var(--white);text-align:center;padding:18px 14px;box-shadow:0 4px 14px rgba(0,0,0,.08)}
.card-cap h3{font-family:"Montserrat",Arial,sans-serif;font-weight:700;font-size:16px;color:var(--ink);margin-bottom:8px}
.card-cap p{font-size:12px;line-height:17px}
.card-cap.feature{background:var(--gold);padding-top:12px}
.card-cap.feature h3{font-size:15px;line-height:19px;margin-bottom:6px}
.card-cap.feature h3,.card-cap.feature p{color:var(--white)}
.practice-edge{left:0;top:1840px;width:1200px;height:90px}

/* professionals */
.team{left:0;top:1920px;width:1200px;height:650px;background:linear-gradient(180deg,#161616 0%,#2b2b2b 60%,#141414 100%)}
.team-title{left:0;top:1968px;color:var(--white)}
.member{top:2060px;width:272px}
.member-photo{width:272px;height:350px;border:6px solid var(--white)}
.member-name{margin-top:16px;text-align:center;font-family:"Montserrat",Arial,sans-serif;font-weight:700;font-size:18px;color:var(--white)}
.member-role{text-align:center;color:var(--gold);font-size:13px;margin-top:4px}
.arrow{top:2196px;width:44px;height:44px;background:var(--white);display:flex;align-items:center;justify-content:center}

/* blog */
.blog-img{left:112px;top:2672px;width:500px;height:420px;background:linear-gradient(135deg,#d9c6a8 0%,#8a7560 50%,#3c3a3a 100%)}
.blog-head{left:688px;top:2668px}
.blog-copy{left:700px;top:2740px;width:420px}
.blog-copy p{margin-bottom:18px}
.blog-btn{left:700px;top:3028px}

/* contact */
.contact{left:0;top:3180px;width:1200px;height:360px;background:linear-gradient(180deg,#fff 0%,var(--cream) 100%)}
.contact-title{left:0;top:3206px}
.field{background:var(--white);border:1px solid #d8d2c8;font-size:12px;color:#888;padding:10px 12px}
.f-name{left:304px;top:3300px;width:184px;height:36px}
.f-email{left:500px;top:3300px;width:184px;height:36px}
.f-phone{left:700px;top:3300px;width:188px;height:36px}
.f-msg{left:304px;top:3350px;width:584px;height:84px}
.submit{left:530px;top:3458px;padding:12px 40px}

/* footer */
.footer{left:0;top:3540px;width:1200px;height:388px;background:var(--black)}
.foot-brand{left:150px;top:3640px;width:320px;text-align:center}
.foot-brand .brand-name{color:var(--white);font-size:36px}
.socials{left:256px;top:3812px;display:flex;gap:14px}
.socials span{width:36px;height:36px;border-radius:50%;background:var(--white)}
.copyright{left:180px;top:3874px;font-size:14px;color:var(--light)}
.foot-h{font-family:"Montserrat",Arial,sans-serif;font-weight:700;font-size:18px;color:var(--white);text-transform:uppercase}
.addr{left:608px;top:3620px;width:260px;color:var(--light)}
.addr-item{display:flex;gap:12px;margin-top:22px;font-size:13px;line-height:19px}
.addr-item svg{flex:none}
.addr-item b{display:block;color:var(--white);font-weight:600;font-size:12px}
.links{left:900px;top:3620px;color:var(--light)}
.links ul{list-style:none;margin-top:20px}
.links li{font-size:14px;line-height:26px}
.links li::before{content:"•";color:var(--white);margin-right:12px}
</style>
</head>
<body>

<!-- HERO -->
<section class="abs hero" role="img" aria-label="Law office interior in warm brown tones"></section>
<div class="abs hero-photo" role="img" aria-label="Senior attorney in a suit standing with arms crossed"></div>
<div class="abs brand-box"><span class="brand-name">Hallorand<br>Trial Firm</span></div>
<nav class="abs nav">
  <a class="active" href="#">HOME</a>
  <a href="#">ABOUT</a>
  <a href="#">PRACTICE AREAS</a>
  <a href="#">PROFESSIONALS</a>
  <a href="#">RESOURCES &amp; ADVISORIES</a>
  <a href="#">BLOG</a>
  <a href="#">CONTACT US</a>
</nav>
<h1 class="abs hero-title">HALLORAND<br>TRIAL FIRM PLLC</h1>
<p class="abs hero-text">We stand beside businesses and entrepreneurs in and out of the courtroom, giving clear counsel and strong trial advocacy in State and Federal Courts.</p>
<a class="abs btn hero-cta" href="#">Connect With Us</a>
<svg class="abs hero-edge" viewBox="0 0 1200 110" preserveAspectRatio="none">
  <polygon points="0,40 1200,70 1200,110 0,110" fill="#fff"/>
  <polygon points="0,40 1200,70 1200,90 0,58" fill="#c49a5e"/>
</svg>

<!-- ABOUT -->
<div class="abs about-brand"><span class="brand-name">Hallorand<br>Trial Firm</span></div>
<h2 class="abs heading section-head about-head">About Us</h2>
<div class="abs copy about-copy">
  <p class="copy-strong">Our attorneys counsel large corporations, small businesses and entrepreneurs facing complex disputes.</p>
  <p>We serve as Florida counsel and trial counsel on product, premises and professional liability, warranty claims and construction defect matters.</p>
  <p>Every case is prepared for trial from day one, so our clients negotiate from a position of strength.</p>
</div>
<a class="abs btn about-btn" href="#">Read More</a>

<!-- PRACTICE AREAS -->
<section class="abs practice"></section>
<h2 class="abs heading center-title practice-title">Practice Areas</h2>

<div class="abs card" style="left:112px">
  <div class="abs card-img" role="img" aria-label="Stacked cardboard product boxes" style="background:linear-gradient(160deg,#e9dcc8,#b88f5e)"></div>
  <div class="abs card-cap"><h3>Product Liability</h3><p>Defending makers and sellers against product claims.</p></div>
</div>
<div class="abs card" style="left:364px">
  <div class="abs card-img" role="img" aria-label="Premises liability sign on a desk" style="background:linear-gradient(160deg,#d8d4cf,#8a8580)"></div>
  <div class="abs card-cap"><h3>Premises Liability</h3><p>Representing owners in injury and safety claims.</p></div>
</div>
<div class="abs card" style="left:616px">
  <div class="abs card-img" role="img" aria-label="Model car on a desk with documents" style="background:linear-gradient(160deg,#cfd6dc,#7e8a94)"></div>
  <div class="abs card-cap feature"><h3>Vehicle and Transportation Liability</h3><p>Fleet and carrier defense.</p></div>
</div>
<div class="abs card" style="left:868px">
  <div class="abs card-img" role="img" aria-label="Professionals reviewing papers at a table" style="background:linear-gradient(160deg,#e6e1d8,#9c9486)"></div>
  <div class="abs card-cap"><h3>Professional Liability</h3><p>Protecting firms facing negligence claims.</p></div>
</div>
<svg class="abs practice-edge" viewBox="0 0 1200 90" preserveAspectRatio="none">
  <polygon points="0,30 1200,0 1200,90 0,90" fill="#1a1a1a"/>
  <polygon points="0,30 1200,0 1200,20 0,52" fill="#c49a5e"/>
</svg>

<!-- PROFESSIONALS -->
<section class="abs team" role="img" aria-label="Dark city skyline at dusk"></section>
<h2 class="abs heading center-title team-title">Our Professionals</h2>
<div class="abs arrow" style="left:56px"><svg width="18" height="14" viewBox="0 0 18 14"><path d="M17 7H2M7 1L1 7l6 6" stroke="#1d1d1d" stroke-width="2" fill="none"/></svg></div>
<div class="abs arrow" style="left:1100px"><svg width="18" height="14" viewBox="0 0 18 14"><path d="M1 7h15M11 1l6 6-6 6" stroke="#1d1d1d" stroke-width="2" fill="none"/></svg></div>

<div class="abs member" style="left:140px">
  <div class="member-photo" role="img" aria-label="Attorney portrait in a blue suit" style="background:linear-gradient(180deg,#9aa7b4,#3d4b5c)"></div>
  <p class="member-name">Marcus Ellery</p><p class="member-role">Attorney</p>
</div>
<div class="abs member" style="left:464px">
  <div class="member-photo" role="img" aria-label="Attorney portrait in a mustard jacket" style="background:linear-gradient(180deg,#c9b79a,#b68a2e)"></div>
  <p class="member-name">Marcus Ellery</p><p class="member-role">Attorney</p>
</div>
<div class="abs member" style="left:788px">
  <div class="member-photo" role="img" aria-label="Attorney portrait in a white shirt and tie" style="background:linear-gradient(180deg,#d8d8d4,#8c8e8a)"></div>
  <p class="member-name">Marcus Ellery</p><p class="member-role">Attorney</p>
</div>

<!-- BLOG -->
<div class="abs blog-img" role="img" aria-label="Legal team meeting around a laptop in an office"></div>
<h2 class="abs heading section-head blog-head">Latest Blog</h2>
<div class="abs copy blog-copy">
  <p class="copy-strong">Recent developments in Florida commercial litigation and what they mean for your business.</p>
  <p>Our attorneys share updates on bid disputes, delay claims and new rulings from State and Federal Courts that affect how companies manage risk.</p>
  <p>Read our success stories and advisories to stay prepared before a dispute begins.</p>
</div>
<a class="abs btn blog-btn" href="#">Read More</a>

<!-- CONTACT -->
<section class="abs contact"></section>
<h2 class="abs heading center-title contact-title">Contact Us</h2>
<div class="abs field f-name">Name</div>
<div class="abs field f-email">Email</div>
<div class="abs field f-phone">Phone</div>
<div class="abs field f-msg">Message</div>
<a class="abs btn submit" href="#">Submit</a>

<!-- FOOTER -->
<footer class="abs footer"></footer>
<div class="abs foot-brand"><span class="brand-name">Hallorand<br>Trial Firm</span></div>
<div class="abs socials" aria-label="Social links"><span></span><span></span><span></span></div>
<p class="abs copyright">©2025 Hallorand Trial Firm. All rights reserved.</p>

<div class="abs addr">
  <h3 class="foot-h">Address</h3>
  <div class="addr-item">
    <svg width="26" height="26" viewBox="0 0 26 26"><circle cx="13" cy="13" r="12" fill="#c49a5e"/><path d="M9 7l3 3-2 2c1 2 2 3 4 4l2-2 3 3-2 2c-5 0-10-5-10-10z" fill="#fff"/></svg>
    <div><b>PHONE NUMBER</b>+1 305 555 0148</div>
  </div>
  <div class="addr-item">
    <svg width="26" height="26" viewBox="0 0 26 26"><circle cx="13" cy="13" r="12" fill="#c49a5e"/><rect x="7" y="9" width="12" height="8" fill="none" stroke="#fff" stroke-width="1.5"/><path d="M7 9l6 5 6-5" stroke="#fff" stroke-width="1.5" fill="none"/></svg>
    <div><b>EMAIL US</b>info@hallorandtrial.com</div>
  </div>
  <div class="addr-item">
    <svg width="26" height="26" viewBox="0 0 26 26"><circle cx="13" cy="13" r="12" fill="#c49a5e"/><path d="M13 6a4.5 4.5 0 0 0-4.5 4.5C8.5 14 13 20 13 20s4.5-6 4.5-9.5A4.5 4.5 0 0 0 13 6z" fill="#fff"/><circle cx="13" cy="10.5" r="1.6" fill="#c49a5e"/></svg>
    <div><b>ADDRESS</b>200 Harbor Plaza, Suite 900,<br>Miami, Florida 33131</div>
  </div>
</div>

<div class="abs links">
  <h3 class="foot-h">Quick Link</h3>
  <ul>
    <li>Home</li><li>About Us</li><li>Practice Areas</li><li>Professionals</li>
    <li>Resources &amp; Advisories</li><li>Blog</li><li>Contact Us</li>
  </ul>
</div>

</body>
</html>
```